Diseñar tarjetas VeltaSoft

Velta Soft is dedicated to activities related to: Cloud, rent servers, page layout & mobile applications. The card must be clean and impressive.

Velta Soft se dedica a actividades relacionadas con: Cloud, renta de servidores, diseño de páginas & aplicaciones móviles. La tarjeta debe de ser limpia e impactante.

You can find the logo, and fonts here: https://www.quillvaultshare.net/sh/3k9tq2mzwlb71xp/BBQyL7hWs4Kc2n9RF5vdTaLpe?dl=0

```html
<!DOCTYPE html>
<html lang="en">
<head>
<meta charset="utf-8">
<title>Velta Soft — Business Card</title>
<link href="https://fonts.googleapis.com/css2?family=Arimo:wght@700&family=Open+Sans:wght@400;600&display=swap" rel="stylesheet">
<style>
  :root {
    --backdrop: #d9d9d9;
    --card: #ffffff;
    --ink: #111111;
    --ink-soft: #333333;
    --shadow: rgba(0, 0, 0, 0.25);
  }
  * { margin: 0; padding: 0; box-sizing: border-box; }
  html, body { width: 1200px; height: 799px; overflow: hidden; }
  body {
    background: var(--backdrop);
    position: relative;
    font-family: "Open Sans", Arial, sans-serif;
    color: var(--ink);
  }
  .card {
    position: absolute;
    top: 240px;
    width: 540px;
    height: 310px;
    background: var(--card);
    border-radius: 26px;
    box-shadow: 0 10px 28px var(--shadow);
  }
  .card--front { left: 45px; }
  .card--back { left: 615px; }

  /* Front */
  .brand {
    position: absolute;
    left: 0;
    right: 0;
    top: 100px;
    display: flex;
    flex-direction: column;
    align-items: center;
  }
  .brand__name {
    font-family: "Open Sans", Arial, sans-serif;
    font-weight: 400;
    font-size: 50px;
    line-height: 1.1;
    color: var(--ink);
    letter-spacing: 0.5px;
    white-space: nowrap;
  }
  .brand__tagline {
    margin-top: 14px;
    font-family: "Arimo", Arial, sans-serif;
    font-weight: 700;
    font-size: 11.5px;
    color: var(--ink);
    white-space: nowrap;
    letter-spacing: 0.1px;
  }

  /* Back */
  .person {
    position: absolute;
    right: 36px;
    top: 88px;
    text-align: right;
  }
  .person__name {
    font-size: 19px;
    font-weight: 400;
    letter-spacing: 0.8px;
    text-transform: uppercase;
    white-space: nowrap;
  }
  .person__role {
    font-size: 9px;
    color: var(--ink-soft);
    margin-top: 2px;
  }
  .contacts {
    position: absolute;
    right: 36px;
    top: 168px;
    list-style: none;
  }
  .contacts__item {
    display: flex;
    justify-content: flex-end;
    align-items: center;
    gap: 10px;
    font-size: 13px;
    height: 24px;
    white-space: nowrap;
  }
  .contacts__icon { width: 16px; height: 16px; flex: none; }
</style>
</head>
<body>
  <section class="card card--front" aria-label="Card front">
    <div class="brand">
      <div class="brand__name">Velta Soft</div>
      <div class="brand__tagline">Related to Cloud, Rent Servers, Page Layout &amp; Mobile Applications.</div>
    </div>
  </section>

  <section class="card card--back" aria-label="Card back">
    <div class="person">
      <div class="person__name">Marcus Hale</div>
      <div class="person__role">CEO</div>
    </div>
    <ul class="contacts">
      <li class="contacts__item">
        <span>+0198765432</span>
        <svg class="contacts__icon" viewBox="0 0 16 16" aria-hidden="true">
          <circle cx="8" cy="8" r="8" fill="#111"/>
          <path d="M5 4.2l1.6-.4 1 2.2-1 .8c.5 1.1 1.3 1.9 2.4 2.4l.8-1 2.2 1-.4 1.6c-3.6.2-6.8-3-6.6-6.6z" fill="#fff"/>
        </svg>
      </li>
      <li class="contacts__item">
        <span>veltasoft@mailbox.com</span>
        <svg class="contacts__icon" viewBox="0 0 16 16" aria-hidden="true">
          <circle cx="8" cy="8" r="8" fill="#111"/>
          <rect x="4" y="5" width="8" height="6" fill="#fff"/>
          <path d="M4 5l4 3.2L12 5" fill="none" stroke="#111" stroke-width="0.9"/>
        </svg>
      </li>
      <li class="contacts__item">
        <span>www.veltasoft.com</span>
        <svg class="contacts__icon" viewBox="0 0 16 16" aria-hidden="true">
          <circle cx="8" cy="8" r="8" fill="#111"/>
          <circle cx="8" cy="8" r="4" fill="none" stroke="#fff" stroke-width="1"/>
          <ellipse cx="8" cy="8" rx="1.7" ry="4" fill="none" stroke="#fff" stroke-width="0.8"/>
          <line x1="4" y1="8" x2="12" y2="8" stroke="#fff" stroke-width="0.8"/>
        </svg>
      </li>
      <li class="contacts__item">
        <span>PO Box- 318, Riverton, Eastvale</span>
        <svg class="contacts__icon" viewBox="0 0 16 16" aria-hidden="true">
          <circle cx="8" cy="8" r="8" fill="#111"/>
          <path d="M8 12.5C6 10 5 8.6 5 7a3 3 0 0 1 6 0c0 1.6-1 3-3 5.5z" fill="#fff"/>
          <circle cx="8" cy="7" r="1.1" fill="#111"/>
        </svg>
      </li>
    </ul>
  </section>
</body>
</html>
```